Business Card Design

I am a video director/cameraman and photographer. I cover documentaries, corporate, government departments, educational and non profits. They could be on Tv, Vidflo or DVD to 10 or 10 thousand ppl. Some have been seen worldwide and won international awards.
I regard myself as bold and saturated...as in I want strong ideas of substance to come through in a film and that the info is valid, interesting and saturates the mind without it being geeky boring.
Need a great logo and layout for cards. My name is Barnaby Tolliver and my company is RT Media Productions.

Must have company name, my name, email, website, phone and type of films I do. I'll supply additional info for the back- which will be companies I have filmed for.

Attach image shows I like the boxes/icons idea but am open to yr ideas...Roar on!
Updates

Reason: I am charged by your designs. This is the first time I have used ths type of service and getting to know you guys is very good value for me. Please keep your creative spirit in this. I want a contemporary logo. Some have shown the way forward and a few need to show a clean, current looking image of my attitude by way of log and design. Thx to you all Barn

Industry/Entity Type

Government

```html
<!DOCTYPE html>
<html lang="en">
<head>
<meta charset="utf-8">
<title>RT Media Productions — Business Card</title>
<link rel="stylesheet" href="https://fonts.googleapis.com/css2?family=Michroma&family=Montserrat:wght@400;500&display=swap">
<style>
  :root {
    --page-bg: #e9e9e9;
    --card-dark: #1e2021;
    --card-dark-edge: #151617;
    --card-light: #ffffff;
    --band: #222425;
    --silver: #d4d6d8;
    --ink: #1c1c1c;
    --band-text: #f2f2f2;
  }
  * { margin: 0; padding: 0; box-sizing: border-box; }
  html, body {
    width: 1166px; height: 1200px; overflow: hidden;
    background: var(--page-bg);
  }
  .canvas {
    width: 1166px; height: 1200px;
    display: flex; flex-direction: column; align-items: center;
    justify-content: center; gap: 40px;
  }
  .card {
    width: 900px; height: 540px; position: relative; overflow: hidden;
    box-shadow: 0 6px 18px rgba(0,0,0,0.18);
  }
  /* Front */
  .card--front {
    background: radial-gradient(ellipse at 40% 45%, #2a2c2d 0%, var(--card-dark) 55%, var(--card-dark-edge) 100%);
    display: flex; align-items: center; justify-content: center;
  }
  .company-name {
    font-family: "Michroma", sans-serif;
    font-size: 40px; color: var(--silver);
    letter-spacing: 2px; text-transform: uppercase;
  }
  /* Back */
  .card--back { background: var(--card-light); }
  .title-band {
    position: absolute; top: 35px; left: 15px; right: 0; height: 118px;
    background: var(--band);
    display: flex; flex-direction: column; align-items: center; justify-content: center;
    gap: 14px;
  }
  .person-name {
    font-family: "Michroma", sans-serif;
    font-size: 42px; color: var(--band-text);
    letter-spacing: 2px; text-transform: uppercase; line-height: 1;
  }
  .roles {
    font-family: "Montserrat", sans-serif; font-weight: 500;
    font-size: 21px; color: var(--band-text);
    letter-spacing: 1.5px; text-transform: uppercase; line-height: 1;
  }
  .roles .sep { margin: 0 18px; }
  .contact-list { position: absolute; left: 75px; top: 280px; list-style: none; }
  .contact-item {
    display: flex; align-items: center; height: 38px; margin-bottom: 46px;
    font-family: "Montserrat", sans-serif; font-weight: 500;
    font-size: 23px; color: var(--ink); letter-spacing: 1.5px; text-transform: uppercase;
  }
  .contact-icon { width: 32px; height: 32px; margin-right: 18px; flex: none; }
</style>
</head>
<body>
<main class="canvas">
  <section class="card card--front" aria-label="Card front">
    <h1 class="company-name">RT Media Productions</h1>
  </section>

  <section class="card card--back" aria-label="Card back">
    <header class="title-band">
      <h2 class="person-name">Barnaby Tolliver</h2>
      <p class="roles">Video Director<span class="sep">|</span>Cameraman<span class="sep">|</span>Photographer</p>
    </header>
    <ul class="contact-list">
      <li class="contact-item">
        <svg class="contact-icon" viewBox="0 0 32 32" aria-hidden="true">
          <rect x="2" y="7" width="28" height="19" fill="var(--ink)"/>
          <path d="M3 8 L16 18 L29 8" fill="none" stroke="#fff" stroke-width="2"/>
        </svg>
        your@mail.com
      </li>
      <li class="contact-item">
        <svg class="contact-icon" viewBox="0 0 32 32" aria-hidden="true">
          <path d="M8 3 L12 3 L14 10 L11 12 Q13 18 20 21 L22 18 L29 20 L29 24 Q28 29 22 28 Q6 24 4 8 Q4 4 8 3 Z" fill="var(--ink)"/>
        </svg>
        0000 - 000 000 000
      </li>
      <li class="contact-item">
        <svg class="contact-icon" viewBox="0 0 32 32" aria-hidden="true">
          <circle cx="16" cy="16" r="14" fill="var(--ink)"/>
          <path d="M3 11 H29 M2 17 H30 M4 23 H28" stroke="#fff" stroke-width="2.2"/>
        </svg>
        www.yourwebsite.com
      </li>
    </ul>
  </section>
</main>
</body>
</html>
```